Business card design for Velvet Harbor

We need business cards designed for our new marketing consulting company, Velvet Harbor. Our services include marketing strategy, go-to-market and launch planning, growth strategy, and execution. We serve medical technology and health technology companies, from startups to well-established growth companies.

The business cards should feel professional, credible, reliable and trustworthy, and should instill confidence. Also bold, creative, and modern.

The design must use the Velvet Harbor logo.

The primary brand color is this orange: #FF5501
A secondary color that you can use is this gray: #282B2D
I would prefer only to use the orange and gray. But if you feel you really need an additional accent color (please use it very sparingly, as little as possible), you can use this blue for small accent purposes: #009FED

Attached are the logo files. The main logo is the one with a little bit of orange on the left and the rest is gray.

The business card should include the following:

Velvet Harbor logo
First name and last name
Title
Email address
Phone number and type (in whatever order looks best for the design
Website (the website does not need to be in the same block as the personal info)

For example:

Nessa Pryle
Founder & Principal
nessa@velvetharbor.com
+1.628.309.4156 mobile (can use "." or spaces in between blocks of numbers)
velvetharbor.com (somewhere on the card, it does not need to be with the personal info; and note that there is no "www." at the beginning)

Note that there will be no address listed on the business card.

Target Market(s)

Executives (CEO, head of marketing, head of sales) at medical technology and health technology companies, mostly in their 40s and older, well-educated, often with advanced degrees. They are strategic thinkers, responsible for budgets, and familiar with P&L. Their comfort with and trust in using outside consultants varies.

Industry/Entity Type

Medical technology and health technology companies.

Contact Information for Business Card

See project description

Font styles to use
Sans Serif

Requirements
Must have
• Logo and see Business card details section above.

```html
<!DOCTYPE html>
<html lang="en">
<head>
<meta charset="utf-8">
<title>Velvet Harbor — Business Card</title>
<link rel="stylesheet" href="https://fonts.googleapis.com/css2?family=Michroma&family=Exo+2:wght@400;500&display=swap">
<style>
  :root {
    --stage: #2e2e2e;
    --card: #000000;
    --orange: #ff5501;
    --white: #ffffff;
    --display: "Michroma", sans-serif;
    --body: "Exo 2", sans-serif;
  }
  * { box-sizing: border-box; margin: 0; padding: 0; }
  html, body {
    width: 1200px; height: 1015px; overflow: hidden;
    background: var(--stage);
  }
  .stage {
    position: relative; width: 1200px; height: 1015px;
  }
  .card {
    position: absolute; left: 220px;
    width: 760px; height: 434px;
    background: var(--card);
    overflow: hidden;
    box-shadow: 0 14px 30px rgba(0,0,0,.45);
  }
  .card--front { top: 58px; }
  .card--back { top: 523px; }

  .edge-stripe {
    position: absolute; left: 0; right: 0; bottom: 0; height: 10px;
    display: flex;
  }
  .edge-stripe__accent { width: 37%; background: var(--orange); }
  .edge-stripe__rest { flex: 1; background: var(--white); margin-left: 4px; }

  /* front */
  .brand {
    position: absolute; left: 0; right: 0; top: 150px;
    display: flex; align-items: center; justify-content: center; gap: 26px;
  }
  .brand__dot {
    width: 22px; height: 22px; border-radius: 50%;
    background: var(--orange);
  }
  .brand__name {
    font-family: var(--display);
    color: var(--white);
    font-size: 38px; line-height: 1.3;
    letter-spacing: 9px;
    text-transform: uppercase;
  }

  /* back */
  .holder {
    position: absolute; left: 56px; top: 64px;
  }
  .holder__tab {
    position: absolute; left: -56px; top: 6px;
    width: 28px; height: 52px;
    background: var(--orange);
    border-radius: 0 26px 26px 0;
  }
  .holder__name {
    font-family: var(--display);
    color: var(--white);
    font-size: 24px; letter-spacing: 5px;
    text-transform: uppercase;
  }
  .holder__title {
    font-family: var(--body);
    color: var(--orange);
    font-size: 20px; margin-top: 2px; letter-spacing: .5px;
  }
  .contact {
    position: absolute; left: 56px; top: 200px;
    list-style: none;
    font-family: var(--body); color: var(--white);
    font-size: 20px;
  }
  .contact__item {
    display: flex; align-items: center; gap: 12px;
    margin-bottom: 12px;
  }
  .contact__icon { width: 28px; height: 28px; flex: none; }
  .back-mark {
    position: absolute; right: 60px; top: 120px;
    font-family: var(--display); color: var(--white);
    font-size: 28px; letter-spacing: 6px; line-height: 1.35;
    text-transform: uppercase; text-align: right;
  }
  .website {
    position: absolute; left: 56px; bottom: 40px;
    font-family: var(--body); font-size: 22px;
    color: var(--orange); letter-spacing: .5px;
  }
</style>
</head>
<body>
<main class="stage">
  <section class="card card--front" aria-label="Card front">
    <div class="brand">
      <span class="brand__dot"></span>
      <span class="brand__name">Velvet<br>Harbor</span>
    </div>
    <div class="edge-stripe"><span class="edge-stripe__accent"></span><span class="edge-stripe__rest"></span></div>
  </section>

  <section class="card card--back" aria-label="Card back">
    <div class="holder">
      <span class="holder__tab"></span>
      <h1 class="holder__name">Nessa Pryle</h1>
      <p class="holder__title">Founder &amp; Principal</p>
    </div>
    <ul class="contact">
      <li class="contact__item">
        <svg class="contact__icon" viewBox="0 0 28 28" aria-hidden="true">
          <circle cx="14" cy="14" r="12.5" fill="none" stroke="#ff5501" stroke-width="1.6"/>
          <rect x="9.5" y="7" width="9" height="14" rx="1.5" fill="none" stroke="#ff5501" stroke-width="1.6"/>
          <circle cx="14" cy="18.2" r="0.9" fill="#ff5501"/>
        </svg>
        <span>+1.628.309.4156</span>
      </li>
      <li class="contact__item">
        <svg class="contact__icon" viewBox="0 0 28 28" aria-hidden="true">
          <circle cx="14" cy="14" r="12.5" fill="none" stroke="#ff5501" stroke-width="1.6"/>
          <rect x="7.5" y="9.5" width="13" height="9" fill="none" stroke="#ff5501" stroke-width="1.6"/>
          <path d="M7.5 9.5 L14 15 L20.5 9.5" fill="none" stroke="#ff5501" stroke-width="1.6"/>
        </svg>
        <span>nessa@velvetharbor.com</span>
      </li>
    </ul>
    <p class="back-mark">Velvet<br>Harbor</p>
    <p class="website">velvetharbor.com</p>
    <div class="edge-stripe"><span class="edge-stripe__accent"></span><span class="edge-stripe__rest"></span></div>
  </section>
</main>
</body>
</html>
```